Harbor Lanterns: Walking Beside Young Ones Through Every Season

This book is about being a good father and how to parent them well so they are fully equipped to launch into the world when they become adults. It is an encouraging and practical guide that acknowledges the difficulties of being a good father and provides strategies for addressing them.

Target Market(s)

My target market is dads, or people that will gift this book to a dad that they know

```html
<!DOCTYPE html>
<html lang="en">
<head>
<meta charset="utf-8">
<title>Harbor Lanterns – Cover Variants</title>
<link href="https://fonts.googleapis.com/css2?family=Playfair+Display:wght@700;900&family=Yellowtail&display=swap" rel="stylesheet">
<style>
  :root {
    --stage: #ffe0ac;
    --teal: #7ccbc9;
    --cream: #f1e2c5;
    --rose: #d8475f;
    --sun: #f9d45c;
    --white: #ffffff;
    --art-blue: #46699a;
    --art-pink: #ef5f80;
  }
  * { box-sizing: border-box; margin: 0; padding: 0; }
  html, body { width: 1200px; height: 1200px; overflow: hidden; }
  body {
    background: var(--stage);
    position: relative;
    font-family: "Playfair Display", Georgia, serif;
  }
  .cover {
    position: absolute;
    top: 211px;
    width: 554px;
    height: 783px;
  }
  .cover--teal { left: 39px; background: var(--teal); }
  .cover--cream { left: 616px; background: var(--cream); }

  .title {
    position: absolute;
    left: 0; right: 0;
    text-align: center;
    color: var(--rose);
    font-weight: 900;
    line-height: 1;
    letter-spacing: -0.5px;
  }
  .title__top { top: 64px; font-size: 46px; }
  .title__main { top: 112px; font-size: 68px; }

  .band {
    position: absolute;
    left: 112px;
    width: 330px;
    height: 32px;
    background: var(--sun);
    color: var(--rose);
    font-weight: 700;
    font-size: 19px;
    line-height: 32px;
    text-align: center;
    letter-spacing: 0.3px;
  }
  .band--first { top: 190px; }
  .band--second { top: 252px; }

  .connector {
    position: absolute;
    top: 224px;
    left: 0; right: 0;
    text-align: center;
    font-family: "Yellowtail", cursive;
    font-size: 22px;
    line-height: 28px;
    color: var(--white);
  }

  .illustration {
    position: absolute;
    left: 90px;
    top: 315px;
    width: 374px;
    height: 372px;
    border-radius: 180px 180px 24px 24px;
    background: radial-gradient(circle at 50% 38%, var(--art-pink) 0%, rgba(239,95,128,0.5) 30%, var(--art-blue) 62%, rgba(70,105,154,0.35) 100%);
  }

  .ribbon {
    position: absolute;
    left: 58px;
    top: 677px;
    width: 438px;
    height: 90px;
  }
  .ribbon__tail { fill: var(--rose); }
  .ribbon__body { fill: var(--rose); }
  .ribbon__name {
    fill: var(--sun);
    font-family: "Playfair Display", Georgia, serif;
    font-weight: 700;
    font-size: 26px;
  }
</style>
</head>
<body>

  <section class="cover cover--teal" aria-label="Book cover, teal variant">
    <h1 class="title title__top">HARBOR</h1>
    <p class="title title__main">LANTERNS</p>
    <p class="band band--first">WALKING BESIDE YOUNG ONES</p>
    <p class="connector">through</p>
    <p class="band band--second">EVERY SEASON</p>
    <div class="illustration" role="img" aria-label="Illustration of a cheerful father flexing his arms with a daughter and son hugging him, surrounded by hearts and a small crown"></div>
    <svg class="ribbon" viewBox="0 0 438 90" aria-label="Author's name ribbon">
      <path class="ribbon__tail" d="M0 46 L36 30 L46 78 L26 86 L32 66 Z"/>
      <path class="ribbon__tail" d="M438 46 L402 30 L392 78 L412 86 L406 66 Z"/>
      <path class="ribbon__body" d="M22 34 Q219 -12 416 34 L404 80 Q219 38 34 80 Z"/>
      <defs><path id="arc-teal" d="M74 60 Q219 22 364 60"/></defs>
      <text class="ribbon__name" text-anchor="middle"><textPath href="#arc-teal" startOffset="50%">AUTHOR'S NAME</textPath></text>
    </svg>
  </section>

  <section class="cover cover--cream" aria-label="Book cover, cream variant">
    <h2 class="title title__top">HARBOR</h2>
    <p class="title title__main">LANTERNS</p>
    <p class="band band--first">WALKING BESIDE YOUNG ONES</p>
    <p class="connector">through</p>
    <p class="band band--second">EVERY SEASON</p>
    <div class="illustration" role="img" aria-label="Illustration of a cheerful father flexing his arms with a daughter and son hugging him, surrounded by hearts and a small crown"></div>
    <svg class="ribbon" viewBox="0 0 438 90" aria-label="Author's name ribbon">
      <path class="ribbon__tail" d="M0 46 L36 30 L46 78 L26 86 L32 66 Z"/>
      <path class="ribbon__tail" d="M438 46 L402 30 L392 78 L412 86 L406 66 Z"/>
      <path class="ribbon__body" d="M22 34 Q219 -12 416 34 L404 80 Q219 38 34 80 Z"/>
      <defs><path id="arc-cream" d="M74 60 Q219 22 364 60"/></defs>
      <text class="ribbon__name" text-anchor="middle"><textPath href="#arc-cream" startOffset="50%">AUTHOR'S NAME</textPath></text>
    </svg>
  </section>

</body>
</html>
```